Real Estate Business Cards

Looking for a clean, sharp and professional look for our Real Estate investment Fund that invests in Multi Family Apartment buildings.

Target Market(s)

Real Estate Fund

Industry/Entity Type

Real Estate

Contact Information for Business Card

Company Description: Real Estate Investment Fund
Company Name: RKW Holdings
Name: Marcus Olvane
Cell: (917) 482-0657
Email: marcus@rkwholdings-example.com
Website: www.rkwholdings-example.com
Address: 418, 9th Street, Brooklyn NY 11218

Colors

Designer to choose colors to be used in the design.

Requirements
Nice to have
• Colors to match logo

```html
<!DOCTYPE html>
<html lang="en">
<head>
<meta charset="utf-8">
<title>RKW Holdings – Business Card</title>
<link href="https://fonts.googleapis.com/css2?family=Lato:wght@400&family=Tinos:wght@400&display=swap" rel="stylesheet">
<style>
  :root {
    --page-bg: #e9eaec;
    --brand-blue: #0e70a8;
    --panel-grey: #464646;
    --seal-white: rgba(250, 250, 250, 0.94);
    --seal-edge: #d8d8d8;
    --text-light: #ffffff;
  }
  html, body {
    margin: 0;
    width: 1200px;
    height: 900px;
    overflow: hidden;
    background: var(--page-bg);
  }
  .business-card {
    position: absolute;
    left: 120px;
    top: 152px;
    width: 960px;
    height: 595px;
    background: var(--brand-blue);
    overflow: hidden;
    box-shadow: 0 10px 30px rgba(0, 0, 0, 0.18);
  }
  .side-panel {
    position: absolute;
    left: 649px;
    top: 0;
    width: 311px;
    height: 100%;
    background: var(--panel-grey);
  }
  .brand-seal {
    position: absolute;
    left: 394px;
    top: 33px;
    width: 516px;
    height: 516px;
    border-radius: 50%;
    background: var(--seal-white);
    box-shadow: 0 2px 6px rgba(0, 0, 0, 0.25);
    border: 1px solid var(--seal-edge);
    display: flex;
    align-items: center;
    justify-content: center;
  }
  .brand-name {
    margin-top: 140px;
    font-family: "Tinos", "Times New Roman", serif;
    font-size: 46px;
    letter-spacing: 1px;
    color: var(--brand-blue);
    text-transform: uppercase;
  }
  .holder-name {
    position: absolute;
    left: 56px;
    top: 66px;
    margin: 0;
    font-family: "Tinos", "Times New Roman", serif;
    font-weight: 400;
    font-size: 38px;
    letter-spacing: 0.5px;
    color: var(--text-light);
    text-transform: uppercase;
  }
  .contact-block {
    position: absolute;
    left: 56px;
    font-family: "Lato", Arial, sans-serif;
    font-size: 19px;
    line-height: 35px;
    color: var(--text-light);
  }
  .address { top: 322px; }
  .contact-lines { top: 427px; }
  .contact-line {
    display: flex;
    align-items: center;
    gap: 8px;
  }
  .contact-line svg {
    width: 20px;
    height: 20px;
    fill: var(--text-light);
    flex: none;
  }
</style>
</head>
<body>
  <div class="business-card">
    <div class="side-panel"></div>

    <h1 class="holder-name">Marcus Olvane</h1>

    <div class="contact-block address">
      <div>418, 9th Street</div>
      <div>Brooklyn NY 11218</div>
    </div>

    <div class="contact-block contact-lines">
      <div class="contact-line">
        <svg viewBox="0 0 20 20" aria-hidden="true"><path d="M2 7c0-2 3-4 8-4s8 2 8 4v1.5h-4V7c-1-.6-2.4-.9-4-.9S7 6.4 6 7v1.5H2z"/><path d="M5 10l2-2h6l2 2 1.5 6.5h-13z M10 10.5a2 2 0 1 0 0 4 2 2 0 1 0 0-4z" fill-rule="evenodd"/></svg>
        <span>(917) 482-0657</span>
      </div>
      <div class="contact-line">
        <svg viewBox="0 0 20 20" aria-hidden="true"><path d="M2 5h16v10H2z M3.5 6.2L10 11l6.5-4.8" fill-rule="evenodd"/><path d="M3 6l7 5 7-5" fill="none" stroke="#0e70a8" stroke-width="1.2"/></svg>
        <span>marcus@rkwholdings-example.com</span>
      </div>
      <div class="contact-line">
        <svg viewBox="0 0 20 20" aria-hidden="true"><circle cx="10" cy="10" r="8"/><path d="M6 5c2 1 1 3 3 3s1 3-1 3-1 3-3 2M12 4c0 2 2 2 3 3M11 16c0-2 2-2 2-4 2 0 3 1 3 2" fill="none" stroke="#0e70a8" stroke-width="1.4"/></svg>
        <span>www.rkwholdings-example.com</span>
      </div>
    </div>

    <div class="brand-seal">
      <div class="brand-name">RKW Holdings</div>
    </div>
  </div>
</body>
</html>
```